KJ Glimmer Cleaning Business Card

We need a business card for our new business, a cleaning company using steam. We already have a logo, and would like a modern-looking card using colors that go well with those in our logo.

```html
<!DOCTYPE html>
<html lang="en">
<head>
<meta charset="utf-8">
<title>KJ Glimmer Cleaning – Business Card</title>
<link href="https://fonts.googleapis.com/css2?family=Noto+Sans:wght@400;700&display=swap" rel="stylesheet">
<style>
  :root {
    --page-bg: #e6e7ea;
    --card-white: #ffffff;
    --brand-blue: #2f4596;
    --brand-blue-light: #3f64ad;
    --brand-blue-dark: #2a3a8c;
    --brand-green: #7cc22b;
    --text-white: #ffffff;
    --shadow: rgba(20, 30, 60, 0.18);
  }
  * { box-sizing: border-box; margin: 0; padding: 0; }
  html, body {
    width: 1200px; height: 900px; overflow: hidden;
    background: var(--page-bg);
    font-family: "Noto Sans", Verdana, sans-serif;
  }
  .canvas {
    width: 1200px; height: 900px;
    display: flex; align-items: center; justify-content: center; gap: 40px;
  }
  .card {
    position: relative;
    width: 540px; height: 309px;
    border-radius: 18px;
    overflow: hidden;
    box-shadow: 0 10px 28px var(--shadow);
  }

  /* Front face */
  .card-front { background: var(--card-white); }
  .card-front .shape-layer { position: absolute; inset: 0; }
  .front-brand {
    position: absolute; left: 168px; top: 44px;
    display: flex; align-items: center; gap: 12px;
  }
  .brand-dot {
    width: 34px; height: 34px; border-radius: 50%;
    background: var(--brand-green);
  }
  .front-brand .brand-name {
    font-size: 22px; font-weight: 700; color: var(--brand-blue);
  }
  .address {
    position: absolute; left: 30px; top: 126px;
    color: var(--text-white); font-size: 12px; line-height: 1.35;
  }
  .contact {
    position: absolute; right: 28px; top: 176px;
    text-align: right; color: var(--text-white);
  }
  .person-name { font-size: 15px; line-height: 1.2; }
  .person-role { font-size: 11px; color: var(--brand-green); margin-bottom: 6px; }
  .contact-line {
    display: flex; justify-content: flex-end; align-items: center; gap: 6px;
    font-size: 12px; line-height: 1.4;
  }
  .contact-icon {
    width: 11px; height: 11px; flex: none;
  }

  /* Back face */
  .card-back {
    background: radial-gradient(ellipse at 45% 40%, var(--brand-blue-light) 0%, var(--brand-blue) 55%, var(--brand-blue-dark) 100%);
  }
  .back-brand {
    position: absolute; left: 70px; top: 96px;
    display: flex; align-items: center; gap: 18px;
  }
  .back-brand .brand-dot { width: 70px; height: 70px; }
  .back-brand .brand-name {
    font-size: 32px; font-weight: 700; color: var(--text-white); line-height: 1.05;
  }
  .back-url {
    position: absolute; left: 72px; bottom: 58px;
    color: var(--text-white); font-size: 14px; letter-spacing: 4px;
  }
</style>
</head>
<body>
<main class="canvas">

  <section class="card card-front" aria-label="Business card front">
    <svg class="shape-layer" viewBox="0 0 540 309" width="540" height="309" aria-hidden="true">
      <path d="M0 108 C 150 120, 330 150, 540 168 L540 309 L0 309 Z" fill="var(--brand-blue)"/>
      <path d="M250 140 C 360 158, 450 166, 540 160" fill="none" stroke="var(--brand-green)" stroke-width="4"/>
    </svg>

    <div class="front-brand">
      <span class="brand-dot"></span>
      <span class="brand-name">KJ Glimmer Cleaning</span>
    </div>

    <address class="address">
      2750 Elm Crest Rd<br>
      Bastrop TX 78900
    </address>

    <div class="contact">
      <p class="person-name">Mara Lindell</p>
      <p class="person-role">Manager</p>
      <p class="contact-line">555 014 2200
        <svg class="contact-icon" viewBox="0 0 12 12" aria-hidden="true"><circle cx="6" cy="6" r="6" fill="var(--brand-green)"/><path d="M3.5 3 L5 3 L5.5 4.6 L4.7 5.3 Q5.5 6.8 6.7 7.4 L7.4 6.6 L9 7.1 L9 8.5 Q5 8.8 3.5 3 Z" fill="#fff"/></svg>
      </p>
      <p class="contact-line">555 014 2201
        <svg class="contact-icon" viewBox="0 0 12 12" aria-hidden="true"><circle cx="6" cy="6" r="6" fill="var(--brand-green)"/><rect x="4.2" y="2.6" width="3.6" height="6.8" rx="0.7" fill="#fff"/></svg>
      </p>
      <p class="contact-line">hello@glimmerclean.com
        <svg class="contact-icon" viewBox="0 0 12 12" aria-hidden="true"><circle cx="6" cy="6" r="6" fill="var(--brand-green)"/><rect x="3" y="4" width="6" height="4.2" fill="#fff"/><path d="M3 4 L6 6.3 L9 4" fill="none" stroke="var(--brand-green)" stroke-width="0.7"/></svg>
      </p>
      <p class="contact-line">www.glimmerclean.com
        <svg class="contact-icon" viewBox="0 0 12 12" aria-hidden="true"><circle cx="6" cy="6" r="6" fill="var(--brand-green)"/><circle cx="6" cy="6" r="3" fill="none" stroke="#fff" stroke-width="0.8"/><path d="M3 6 H9 M6 3 V9" stroke="#fff" stroke-width="0.6"/></svg>
      </p>
    </div>
  </section>

  <section class="card card-back" aria-label="Business card back">
    <div class="back-brand">
      <span class="brand-dot"></span>
      <span class="brand-name">KJ Glimmer<br>Cleaning</span>
    </div>
    <p class="back-url">www.glimmerclean.com</p>
  </section>

</main>
</body>
</html>
```